Flyer for Medical practice welcoming new patients

We need a DL size brochure designed for Medical practice to advertise that we are accepting new patients. Our practice has special interests in women's and children's health and seniors health. Our existing advertising materials are in the colour scheme of purples I have uploaded our logo which includes our colour scheme.

Target Market(s)

Versatile to target anyone looking for a small medical practice that offers continuous care of seeing the same Doctor every time

Industry/Entity Type

Advertising

Font styles to use
Serif

Colors
6b449b
876aae
b7a5cc

Requirements
Must have
• The practice logo of just the picture not Dr Wanda Thorpe.
• Purple colour scheme.
• Practice name: Bramblecote Medical Practice.
• Address: 147 Tolley Rd, Bramblecote NSW 2500.
• Phone: 4371 5806.
• DL size brochure
• Welcoming new patients ( a strong emphasis needs to be placed on this)
• Nurse and onsite ECG's and lung function tests.
• Travel vaccines including yellow fever
• Bulk billing for tertiary students
• We would also like design to alter the text so that we can change the points to be reflect who we are targeting at the time.
Nice to have
• The practice logo with Dr Wanda Thorpe somewhere not as a feature as the practice no longer goes under this name but is still well known as Dr Thorpe's.

```html
<!DOCTYPE html>
<html lang="en">
<head>
<meta charset="utf-8">
<title>Bramblecote Medical Practice – DL Flyer</title>
<link href="https://fonts.googleapis.com/css2?family=Oswald:wght@700&family=Lato:ital,wght@0,400;0,700;0,900;1,700&display=swap" rel="stylesheet">
<style>
  :root{
    --purple-deep:#4e2a86;
    --purple:#6b449b;
    --purple-mid:#876aae;
    --purple-light:#b7a5cc;
    --purple-ink:#432873;
    --lavender-text:#d9c9ec;
    --ink:#2e2e2e;
    --paper:#ffffff;
    --paper-shade:#e4e4e4;
    --backdrop:#2b2b2b;
  }
  *{box-sizing:border-box;margin:0;padding:0}
  html,body{width:902px;height:1200px;overflow:hidden}
  body{background:var(--backdrop);position:relative;font-family:"Lato",sans-serif}
  .flyer{
    position:absolute;left:189px;top:62px;width:525px;height:1078px;
    background:linear-gradient(90deg,var(--paper-shade),var(--paper) 30%,var(--paper) 70%,var(--paper-shade));
    overflow:hidden;
  }
  .title-band{
    position:absolute;left:0;top:22px;width:100%;height:202px;
    background:linear-gradient(180deg,var(--purple) 0%,var(--purple-deep) 100%);
    display:flex;align-items:center;justify-content:center;text-align:center;
  }
  .practice-title{
    font-family:"Oswald",sans-serif;font-weight:700;color:var(--paper);
    font-size:50px;line-height:1.18;letter-spacing:.5px;text-transform:uppercase;
    text-shadow:3px 3px 3px rgba(30,10,60,.75);
  }
  .call-band{
    position:absolute;left:0;top:224px;width:100%;height:70px;
    background:var(--purple-light);
    display:flex;align-items:center;justify-content:center;
  }
  .call-band p{font-weight:900;font-size:44px;color:var(--purple-ink);letter-spacing:-.3px}
  .intro{
    position:absolute;left:20px;right:20px;top:356px;text-align:center;
    font-size:22.5px;line-height:1.33;color:var(--ink);
  }
  .intro strong{font-weight:700}
  .welcome-band{
    position:absolute;left:0;top:500px;width:100%;height:66px;
    background:linear-gradient(180deg,var(--purple-mid),var(--purple-light));
    display:flex;align-items:center;justify-content:center;
  }
  .welcome-band h2{
    font-style:italic;font-weight:700;font-size:34px;color:var(--paper);
    text-shadow:2px 2px 3px rgba(40,15,80,.7);
  }
  .services{
    position:absolute;left:0;top:566px;width:100%;height:240px;
  }
  .services svg{position:absolute;left:0;top:0;width:100%;height:240px}
  .service-list{
    position:absolute;left:20px;right:20px;top:18px;list-style:none;text-align:center;
    font-style:italic;font-weight:700;font-size:19px;line-height:1.5;color:var(--lavender-text);
  }
  .service-list li{margin-bottom:11px}
  .service-list li::before{content:"";display:inline-block;width:8px;height:8px;border-radius:50%;background:var(--paper);margin-right:14px;vertical-align:3px}
  .doctor-mark{
    position:absolute;left:0;top:830px;width:100%;height:120px;
    display:flex;align-items:center;justify-content:center;gap:22px;
  }
  .doctor-mark .ring{width:96px;height:96px;border-radius:50%;border:3px solid var(--purple-light)}
  .doctor-mark .name{font-family:"Lato",sans-serif;font-weight:400;font-size:46px;color:var(--purple)}
  .footer{position:absolute;left:0;bottom:0;width:100%;height:118px}
  .footer svg{position:absolute;left:0;top:0;width:100%;height:118px}
  .address{
    position:absolute;left:0;right:0;top:46px;text-align:center;color:var(--paper);
    font-size:17px;line-height:1.55;font-weight:700;
  }
  .address .practice{display:inline-flex;align-items:center;gap:12px;letter-spacing:.3px}
  .address .home-icon{width:20px;height:20px}
  .address span.line{display:block;padding-left:30px}
</style>
</head>
<body>
  <main class="flyer">
    <header class="title-band">
      <h1 class="practice-title">Bramblecote<br>Medical Practice</h1>
    </header>

    <section class="call-band"><p>Call us 4371 5806</p></section>

    <p class="intro">We are an award winning accredited practice which provides a comprehensive range of services, which <strong>promote quality and continuity of care</strong></p>

    <section class="welcome-band"><h2>Welcoming New Patients</h2></section>

    <section class="services">
      <svg viewBox="0 0 525 240" preserveAspectRatio="none" aria-hidden="true">
        <path d="M0 0H525V208Q262 262 0 208Z" fill="var(--purple-light)"/>
        <path d="M0 0H525V200Q262 248 0 200Z" fill="var(--purple)"/>
      </svg>
      <ul class="service-list">
        <li>Nurse on site to do ECG's, lung function tests,<br>health assessments and much more</li>
        <li>Travel vaccines including yellow fever</li>
        <li>Bulk billing for tertiary students</li>
        <li>Easy on street parking</li>
      </ul>
    </section>

    <div class="doctor-mark">
      <span class="ring"></span>
      <span class="name">Dr Wanda Thorpe</span>
    </div>

    <footer class="footer">
      <svg viewBox="0 0 525 118" preserveAspectRatio="none" aria-hidden="true">
        <path d="M0 30Q262 -14 525 30V118H0Z" fill="var(--purple-light)"/>
        <path d="M0 38Q262 0 525 38V118H0Z" fill="var(--purple)"/>
      </svg>
      <div class="address">
        <span class="practice">
          <svg class="home-icon" viewBox="0 0 20 20" aria-hidden="true"><circle cx="10" cy="10" r="10" fill="#111"/><path d="M10 4.5L4.5 9.5H6V15H9V12H11V15H14V9.5H15.5Z" fill="#fff"/></svg>
          BRAMBLECOTE MEDICAL PRACTICE
        </span>
        <span class="line">147 Tolley Rd, Bramblecote NSW 2500</span>
      </div>
    </footer>
  </main>
</body>
</html>
```